Flyer for an IT consultancy firm

We are an IT consultancy firm based in Iceland. We have a website at: www.brimvolt.com where you can get acquainted with our activities.
We require a double-sided flyer in A4 format to be handed out in conferences, trade shows etc. The flyer is basically a summarized overview of our range of services.

The deliverable should incorporate some visual elements that are relevant to our line of business such as:
• computers
• cybersecurity
• networks
Also, it would be nice to have visuals relating to Icelandic geography, to further emphasize our local roots. Some suggested keywords:
• volcano
• aurora borealis
• waterfall
• glacier

NB: the flyer will be printed out, therefore image resolution needs to be high enough to render nicely on paper.
The primary colors would be red, black and white – in line with our logo. But there is freedom to diverge and go for a different color scheme.

The logo should be present on the top front of the flyer. The URL www.brimvolt.com needs to be mentioned prominently, for example at the bottom of the page.

Examples of design we like:
• https://www.pixelbazaar.net/design/24252027
• https://www.pixelbazaar.net/design/24291120

Attached:
• the text for the brochure in PDF format
• our logo in vector format

IT, software, cybersecurity

EB3D1F
EC4F4E
F09395
F8D3D4
FCEDEE

• existing logo, and visuals related to computer, networks etc
• Icelandic geography/landscapes

```html
<!DOCTYPE html>
<html lang="en">
<head>
<meta charset="utf-8">
<title>Brimvolt Flyer – Front and Back</title>
<link href="https://fonts.googleapis.com/css2?family=Open+Sans:wght@300;400;600;700&display=swap" rel="stylesheet">
<style>
:root{
  --stage:#3a3a3c;
  --red:#c0161c;
  --red-deep:#8e0d12;
  --red-bright:#eb3d1f;
  --coral:#ec4f4e;
  --pink:#f09395;
  --blush:#f8d3d4;
  --blush-light:#fcedee;
  --ink:#111111;
  --white:#ffffff;
  --grey:#8a8d92;
}
*{box-sizing:border-box;margin:0;padding:0}
html,body{width:1200px;height:636px;overflow:hidden;background:var(--stage);font-family:"Open Sans",Arial,sans-serif}
.stage{position:relative;width:1200px;height:636px}
.option-label{position:absolute;top:80px;color:#f2f2f2;font-weight:700;font-size:13px;text-align:center;width:301px}
.page{position:absolute;top:114px;width:645px;height:911px;transform:scale(.4658);transform-origin:0 0;overflow:hidden;box-shadow:0 22px 30px rgba(0,0,0,.55)}
.page-front-black{left:130px;background:var(--ink)}
.page-front-white{left:466px;background:var(--white)}
.page-back{left:809px;background:var(--white)}
.abs{position:absolute}

/* front */
.hero-sky{left:0;top:0;width:645px;height:175px;background:linear-gradient(90deg,#f4f4f6 0%,#dfe3ec 45%,#8d97b4 80%,#6e7ea5 100%)}
.brand{left:48px;top:40px;display:flex;align-items:center;gap:16px}
.brand-dot{width:86px;height:86px;border-radius:50%;border:6px solid var(--red)}
.brand-name{font-weight:700;font-size:46px;color:var(--red);letter-spacing:1px}
.hero-art{left:0;top:158px}
.headline{right:40px;top:182px;text-align:right;color:var(--white);font-weight:700;font-size:29px;line-height:35px}
.tagline{right:40px;top:376px;text-align:right;color:var(--white);font-weight:300;font-size:20px;line-height:25px}
.url-tab{left:34px;top:502px;color:var(--white);font-weight:700;font-size:19px}
.intro-title{left:37px;top:554px;font-weight:700;font-size:19px;line-height:25px}
.intro-body{left:37px;top:614px;width:262px;font-size:11.4px;line-height:15.6px;text-align:justify}
.divider{left:325px;top:558px;height:258px;border-left:1px dashed #777}
.work-photo{left:350px;top:558px;width:255px;height:282px;background:linear-gradient(160deg,#2c3036,#121417 55%,#5a4232)}
.cta{left:32px;top:757px;width:261px;height:84px;background:var(--coral);border-radius:4px;padding:9px 12px;color:var(--white);font-weight:700;font-size:18px;line-height:22px}
.footer-band{left:0;top:862px}
.footer-text{top:867px;color:var(--white);font-size:14px;font-weight:700}
.footer-brand{left:455px;top:857px;display:flex;align-items:center;gap:8px}
.footer-brand .brand-dot{width:36px;height:36px;border-width:3px}
.footer-brand .brand-name{font-size:19px}
.page-front-black .intro-title,.page-front-black .intro-body{color:var(--white)}
.page-front-white .intro-title,.page-front-white .intro-body{color:var(--ink)}
.page-front-black .footer-brand .brand-name{color:var(--white)}
.page-front-white .footer-brand .brand-name{color:var(--ink)}
.page-front-black .footer-brand .brand-dot{border-color:var(--white)}
.page-front-white .footer-brand .brand-dot{border-color:var(--ink)}

/* back */
.strip-photo{top:0;height:135px}
.visit-band{left:0;top:135px;width:645px;height:40px;background:linear-gradient(90deg,var(--red) 0%,var(--red-deep) 100%);color:var(--white);text-align:center;font-size:14px;font-weight:700;line-height:40px}
.visit-band .visit-url{font-size:20px;margin-left:4px;letter-spacing:.5px}
.col-right-bg{left:323px;top:175px;width:322px;height:736px;background:linear-gradient(180deg,var(--blush) 0%,var(--blush-light) 100%)}
.service{width:268px}
.service h3{color:var(--red);font-size:18.5px;font-weight:700;line-height:19px;margin-bottom:10px}
.service p{font-size:10.2px;line-height:14px;color:#333;text-align:justify;margin-bottom:10px}
.rule{left:36px;width:287px;border-top:2px solid var(--blush)}
.server-photo{left:36px;top:521px;width:267px;height:148px;background:linear-gradient(120deg,#1b2a55,#3f5aa8 60%,#6d5f55)}
.caption{left:36px;top:673px;font-size:10px;color:#333}
.security-box{left:340px;top:550px;width:266px;height:242px;background:var(--red-bright);border-radius:4px;padding:10px}
.security-box h3{color:var(--white);margin-bottom:10px}
.security-box p{color:var(--white)}
.back-brand{left:420px;top:812px;display:flex;align-items:center;gap:8px}
.back-brand .brand-dot{width:46px;height:46px;border-width:4px}
.back-brand .brand-name{font-size:22px;color:var(--ink)}
.call-us{left:412px;top:862px;font-size:15px;font-weight:700;color:var(--ink)}
.call-us span{font-size:19px}
</style>
</head>
<body>
<div class="stage">
  <div class="option-label" style="left:142px">Front _Black Option</div>
  <div class="option-label" style="left:478px">Front _White Option</div>
  <div class="option-label" style="left:808px">Back</div>

  <!-- front, dark variant -->
  <section class="page page-front-black">
    <div class="abs hero-sky" role="img" aria-label="City skyline at dusk with glowing network lines"></div>
    <div class="abs brand"><div class="brand-dot"></div><div class="brand-name">BRIMVOLT</div></div>
    <svg class="abs hero-art" width="645" height="380" viewBox="0 158 645 380">
      <rect x="0" y="170" width="470" height="355" fill="#8a8f96" role="img" aria-label="Smiling young consultant at a laptop in a bright office"/>
      <polygon points="320,160 350,160 495,525 465,525" fill="var(--grey)"/>
      <polygon points="350,160 645,158 645,525 495,525" fill="var(--red)"/>
      <polygon points="0,497 220,497 240,530 0,530" fill="var(--red-deep)"/>
    </svg>
    <div class="abs headline">Your Icelandic<br>Partner in<br>Cybersecurity<br>and IT<br>Consultancy</div>
    <div class="abs tagline">We transform<br>operational<br>challenges into<br>bespoke IT<br>solutions.</div>
    <div class="abs url-tab">www.brimvolt.com</div>
    <div class="abs intro-title">Brimvolt ehf –<br>Your Icelandic IT partner</div>
    <p class="abs intro-body">Step into a world of comprehensive IT solutions tailored to your unique needs. Our services, available on a contract or as-needed basis, are designed to empower your business and equip you with the tools you need to succeed. More than just a list of offerings, they’re a commitment to quality, a dedication to innovation, and a promise of reliability</p>
    <div class="abs divider"></div>
    <div class="abs work-photo" role="img" aria-label="Hands typing on a keyboard in front of monitors showing code"></div>
    <div class="abs cta">Get in touch with us today to discuss your IT needs in strict confidence.</div>
    <svg class="abs footer-band" width="440" height="28" viewBox="0 0 440 28">
      <polygon points="0,0 130,0 140,14 130,28 0,28" fill="var(--red)"/>
      <polygon points="134,0 280,0 290,14 280,28 134,28 144,14" fill="var(--red)"/>
      <polygon points="284,0 420,0 432,14 420,28 284,28 294,14" fill="var(--red)"/>
      <polygon points="424,0 430,0 440,14 430,28 424,28 434,14" fill="var(--pink)"/>
    </svg>
    <div class="abs footer-text" style="left:37px">Brimvolt ehf</div>
    <svg class="abs" style="left:146px;top:872px" width="16" height="11" viewBox="0 0 16 11"><rect x="0.5" y="0.5" width="15" height="10" fill="#fff"/><polyline points="0.5,0.5 8,6 15.5,0.5" fill="none" stroke="#c0161c"/></svg>
    <div class="abs footer-text" style="left:166px;font-size:12px;font-weight:400;top:869px">info@brimvolt.com</div>
    <svg class="abs" style="left:291px;top:871px" width="15" height="13" viewBox="0 0 15 13"><path d="M1 5 Q7.5 -1 14 5 L12 7 L10 5 L5 5 L3 7 Z M4 7 H11 L12 12 H3 Z" fill="#fff"/></svg>
    <div class="abs footer-text" style="left:308px;font-size:15px">+354 5550142</div>
    <div class="abs footer-brand"><div class="brand-dot"></div><div class="brand-name">BRIMVOLT</div></div>
  </section>

  <!-- front, light variant -->
  <section class="page page-front-white">
    <div class="abs hero-sky" role="img" aria-label="City skyline at dusk with glowing network lines"></div>
    <div class="abs brand"><div class="brand-dot"></div><div class="brand-name">BRIMVOLT</div></div>
    <svg class="abs hero-art" width="645" height="380" viewBox="0 158 645 380">
      <rect x="0" y="170" width="470" height="355" fill="#8a8f96" role="img" aria-label="Smiling young consultant at a laptop in a bright office"/>
      <polygon points="320,160 350,160 495,525 465,525" fill="var(--ink)"/>
      <polygon points="350,160 645,158 645,525 495,525" fill="var(--red)"/>
      <polygon points="0,497 220,497 240,530 0,530" fill="var(--red-deep)"/>
    </svg>
    <div class="abs headline">Your Icelandic<br>Partner in<br>Cybersecurity<br>and IT<br>Consultancy</div>
    <div class="abs tagline">We transform<br>operational<br>challenges into<br>bespoke IT<br>solutions.</div>
    <div class="abs url-tab">www.brimvolt.com</div>
    <div class="abs intro-title">Brimvolt ehf –<br>Your Icelandic IT partner</div>
    <p class="abs intro-body">Step into a world of comprehensive IT solutions tailored to your unique needs. Our services, available on a contract or as-needed basis, are designed to empower your business and equip you with the tools you need to succeed. More than just a list of offerings, they’re a commitment to quality, a dedication to innovation, and a promise of reliability</p>
    <div class="abs divider"></div>
    <div class="abs work-photo" role="img" aria-label="Hands typing on a keyboard in front of monitors showing code"></div>
    <div class="abs cta">Get in touch with us today to discuss your IT needs in strict confidence.</div>
    <svg class="abs footer-band" width="440" height="28" viewBox="0 0 440 28">
      <polygon points="0,0 130,0 140,14 130,28 0,28" fill="var(--red)"/>
      <polygon points="134,0 280,0 290,14 280,28 134,28 144,14" fill="var(--red)"/>
      <polygon points="284,0 420,0 432,14 420,28 284,28 294,14" fill="var(--red)"/>
      <polygon points="424,0 430,0 440,14 430,28 424,28 434,14" fill="var(--pink)"/>
    </svg>
    <div class="abs footer-text" style="left:37px">Brimvolt ehf</div>
    <svg class="abs" style="left:146px;top:872px" width="16" height="11" viewBox="0 0 16 11"><rect x="0.5" y="0.5" width="15" height="10" fill="#fff"/><polyline points="0.5,0.5 8,6 15.5,0.5" fill="none" stroke="#c0161c"/></svg>
    <div class="abs footer-text" style="left:166px;font-size:12px;font-weight:400;top:869px">info@brimvolt.com</div>
    <svg class="abs" style="left:291px;top:871px" width="15" height="13" viewBox="0 0 15 13"><path d="M1 5 Q7.5 -1 14 5 L12 7 L10 5 L5 5 L3 7 Z M4 7 H11 L12 12 H3 Z" fill="#fff"/></svg>
    <div class="abs footer-text" style="left:308px;font-size:15px">+354 5550142</div>
    <div class="abs footer-brand"><div class="brand-dot"></div><div class="brand-name">BRIMVOLT</div></div>
  </section>

  <!-- back -->
  <section class="page page-back">
    <div class="abs strip-photo" style="left:0;width:195px;background:linear-gradient(135deg,#2a2e33,#5b5f66)" role="img" aria-label="Developer typing at a workstation with code on screen"></div>
    <div class="abs strip-photo" style="left:197px;width:188px;background:linear-gradient(135deg,#1d3c5a,#4d86a8)" role="img" aria-label="Analytics dashboard with charts on a monitor"></div>
    <div class="abs strip-photo" style="left:387px;width:258px;background:linear-gradient(135deg,#7d8a86,#1f5a3e)" role="img" aria-label="Close-up of a circuit board with a heat sink"></div>
    <div class="abs visit-band">Please visit Our Website : <span class="visit-url">www.brimvolt.com</span></div>
    <div class="abs col-right-bg"></div>

    <div class="abs service" style="left:36px;top:202px">
      <h3>Software Development and Integration Services</h3>
      <p>We specialize in custom software development across different platforms (Linux, Windows, embedded systems). We are open source software advocates, and leverage decades of experience to deliver innovative and cost-effective solutions tailored to your needs.</p>
      <p>Let’s build the perfect software solution for you.</p>
    </div>
    <div class="abs rule" style="top:366px"></div>
    <div class="abs service" style="left:36px;top:376px">
      <h3>Infrastructure Monitoring Services</h3>
      <p>Do you know what is really going on inside your systems? We leverage leading open source monitoring solutions to bring visibility to your infrastructure. Monitor your systems proactively to ensure that they remain healthy at all times. Collect logs in real time and be notified when problems occur or warnings are raised.</p>
    </div>
    <div class="abs server-photo" role="img" aria-label="Engineer with a laptop in a server room aisle"></div>
    <div class="abs caption">Fix issues before they become problems.</div>
    <div class="abs rule" style="top:697px"></div>
    <div class="abs service" style="left:36px;top:714px">
      <h3>Technology Assessment Services</h3>
      <p>Unsure about which tools are right for you or what IT strategy to pursue to help your business grow? We conduct market research and perform technical evaluations of software and hardware products to determine the best solutions for your company.</p>
      <p>Let’s empower your business with leading-edge solutions.</p>
    </div>

    <div class="abs service" style="left:344px;top:202px">
      <h3>Systems Administration</h3>
      <p>Are you having trouble with your IT infrastructure and in need of qualified personnel to take care of them? Or do you simply need a watchful and expert eye to ensure your systems keep running smoothly? We provide on-site and remote sysadmin services to manage your systems and bring you peace of mind.</p>
      <p>Take back control</p>
    </div>
    <div class="abs service" style="left:344px;top:376px">
      <h3>Automation</h3>
      <p>Because you need effective tools to grow and prosper, it is essential that your IT systems align with your operational needs. We offer a comprehensive review of your business and IT environment so as to optimize the means already at your disposal. We streamline your workflow and develop new tools as needed, to make your IT systems work harder for you.</p>
      <p>Let us automate the boring stuff for you.</p>
    </div>
    <div class="abs security-box service">
      <h3>Security Services</h3>
      <p>We understand the importance of security in today’s digital landscape. That’s why we offer comprehensive security services, including network audits to find and remedy flaws before they can be exploited to your disadvantage.</p>
      <p>We perform a thorough review of your IT environment to identify and remediate the weak spots, in order to keep your business secure, protect your assets and your reputation. Let’s raise your security posture to the highest standards, so that you don’t become the next victim – or headline.</p>
      <p>Bring the good guys in to keep the bad guys out.</p>
    </div>
    <div class="abs back-brand"><div class="brand-dot"></div><div class="brand-name">BRIMVOLT</div></div>
    <div class="abs call-us">Call Us: <span>+354 5550142</span></div>
    <svg class="abs" style="left:0;top:893px" width="645" height="18" viewBox="0 0 645 18">
      <polygon points="320,18 340,0 645,0 645,18" fill="var(--red)"/>
    </svg>
  </section>
</div>
</body>
</html>
```